Executive Business Consulting for Telco Companies and Telco Start up companies

1.) Looking for an appealing and action oriented business card design.
2.)The target companies to work with start-ups and existing companies that focus on Business to Business applications
3.) For "OLRA", a Belgium based Executive consultancy company specialised in global reach starting from the centre of Europe = Brussels.
4.) Our core competence is the Go To Market in All major global regions, incl North America, Latin America, Asia, Japan, Europe and Africa.
5.) Design should be appealing to CEO, CFO and Venture Funds signalling; Expertise, Stability, Maturity and Commitment
6.) Preferred color scheme is Blue focussed and using a modern FONT.
7.) Logo design is included (uploaded)

Target Market(s)

Telecommunication Market. Companies in a B2B business model, developping services or applications to make business run more profitable

Industry/Entity Type

Business

Contact Information for Business Card

Company Name: OLRA
Name: Joris Vandekamp
Titel: Managing Director
Address: Lindelaan 58 , B-9120 Haasdonk , Belgium
Tel: + 32 471 283 915
Email: joris_vandekamp@mailbox-example.com
LinkedIn: be.profilenet-example.com/in/jorisvandekamp/

Font styles to use
Serif

Colors
0455a3
3277b5

Requirements
Must have
• Second Side Text: Execute Sales Strategy and Transformation

```html
<!DOCTYPE html>
<html lang="en">
<head>
<meta charset="utf-8">
<title>OLRA business card</title>
<link href="https://fonts.googleapis.com/css2?family=Lora:ital,wght@0,400;0,500;0,700;1,400&display=swap" rel="stylesheet">
<style>
  :root {
    --page-bg: #e4e4e4;
    --band-grey: #4a4b4d;
    --card-white: #f2f2f2;
    --brand-navy: #1d3557;
    --brand-blue: #3277b5;
    --accent-blue: #2a88cc;
    --text-grey: #3a3a3a;
    --text-dark: #222222;
  }
  html, body {
    margin: 0;
    padding: 0;
    width: 1200px;
    height: 1000px;
    overflow: hidden;
    background: var(--page-bg);
    font-family: "Lora", serif;
  }
  .card {
    position: absolute;
    top: 190px;
    width: 400px;
    height: 620px;
    box-shadow: 0 6px 18px rgba(0,0,0,0.18);
  }
  .card-front { left: 150px; }
  .card-back { left: 650px; }
  .card-shape {
    position: absolute;
    inset: 0;
    width: 400px;
    height: 620px;
  }
  .wordmark {
    position: absolute;
    display: flex;
    align-items: center;
    gap: 12px;
    color: var(--brand-navy);
    font-weight: 700;
    line-height: 1;
  }
  .wordmark-dot {
    border-radius: 50%;
    background: var(--brand-blue);
  }
  .card-front .wordmark {
    top: 190px;
    left: 0;
    right: 0;
    justify-content: center;
    font-size: 80px;
    letter-spacing: 2px;
  }
  .card-front .wordmark-dot { width: 40px; height: 40px; }
  .tagline {
    position: absolute;
    top: 292px;
    left: 70px;
    right: 70px;
    margin: 0;
    text-align: center;
    font-size: 15px;
    font-style: italic;
    font-weight: 400;
    line-height: 22px;
    color: var(--brand-blue);
  }
  .card-back .wordmark {
    top: 64px;
    right: 50px;
    font-size: 38px;
    letter-spacing: 1px;
    gap: 8px;
  }
  .card-back .wordmark-dot { width: 20px; height: 20px; }
  .person {
    position: absolute;
    top: 150px;
    right: 50px;
    text-align: right;
  }
  .person-name {
    margin: 0;
    font-size: 22px;
    font-weight: 700;
    color: var(--text-grey);
  }
  .person-title {
    margin: 4px 0 0;
    font-size: 15px;
    font-weight: 500;
    color: var(--accent-blue);
  }
  .contact-list {
    position: absolute;
    top: 382px;
    left: 36px;
    width: 330px;
    margin: 0;
    padding: 0;
    list-style: none;
    font-size: 12px;
    font-weight: 400;
    color: var(--text-dark);
    line-height: 16px;
  }
  .contact-list li {
    display: flex;
    align-items: flex-start;
    gap: 22px;
    margin-bottom: 14px;
  }
  .contact-icon {
    flex: 0 0 24px;
    width: 24px;
    height: 24px;
    margin-top: -4px;
  }
  .contact-email, .contact-web { font-size: 11px; }
  .contact-text { white-space: nowrap; }
</style>
</head>
<body>

<section class="card card-front" aria-label="Card front">
  <svg class="card-shape" viewBox="0 0 400 620" aria-hidden="true">
    <rect width="400" height="620" fill="var(--band-grey)"/>
    <polygon points="30,0 370,0 370,330 345,365 345,620 55,620 55,365 30,330" fill="var(--card-white)"/>
  </svg>
  <div class="wordmark">
    <span class="wordmark-text">OLRA</span>
    <span class="wordmark-dot"></span>
  </div>
  <p class="tagline">Execute Sales Strategy and Transformation</p>
</section>

<section class="card card-back" aria-label="Card back">
  <svg class="card-shape" viewBox="0 0 400 620" aria-hidden="true">
    <rect width="400" height="620" fill="var(--band-grey)"/>
    <polygon points="0,0 400,0 400,250 370,285 370,620 0,620" fill="var(--card-white)"/>
    <polygon points="0,270 30,270 30,620 0,620" fill="var(--band-grey)"/>
    <polygon points="30,320 70,345 70,620 30,620" fill="var(--accent-blue)"/>
  </svg>

  <div class="wordmark">
    <span class="wordmark-text">OLRA</span>
    <span class="wordmark-dot"></span>
  </div>

  <div class="person">
    <p class="person-name">Joris Vandekamp</p>
    <p class="person-title">Managing Director</p>
  </div>

  <ul class="contact-list">
    <li class="contact-address">
      <svg class="contact-icon" viewBox="0 0 28 28" aria-hidden="true">
        <polygon points="14,1 26,7.5 26,20.5 14,27 2,20.5 2,7.5" fill="var(--brand-blue)"/>
        <path d="M14 7a5 5 0 0 0-5 5c0 4 5 9 5 9s5-5 5-9a5 5 0 0 0-5-5z" fill="#fff"/>
        <circle cx="14" cy="12" r="1.8" fill="var(--brand-blue)"/>
      </svg>
      <span class="contact-text">Lindelaan 58 , B-9120 Haasdonk ,<br>Belgium</span>
    </li>
    <li class="contact-phone">
      <svg class="contact-icon" viewBox="0 0 28 28" aria-hidden="true">
        <polygon points="14,1 26,7.5 26,20.5 14,27 2,20.5 2,7.5" fill="var(--brand-blue)"/>
        <path d="M10 8c1 0 2 2 2 3s-1 1-1 2 3 4 4 4 1-1 2-1 3 1 3 2-1 2-2 2c-4 0-9-5-9-9 0-1 0-3 1-3z" fill="#fff"/>
      </svg>
      <span class="contact-text">+ 32 471 283 915</span>
    </li>
    <li class="contact-email">
      <svg class="contact-icon" viewBox="0 0 28 28" aria-hidden="true">
        <polygon points="14,1 26,7.5 26,20.5 14,27 2,20.5 2,7.5" fill="var(--brand-blue)"/>
        <rect x="8" y="10" width="12" height="8" fill="none" stroke="#fff" stroke-width="1.4"/>
        <polyline points="8,10 14,15 20,10" fill="none" stroke="#fff" stroke-width="1.4"/>
      </svg>
      <span class="contact-text">joris_vandekamp@mailbox-example.com</span>
    </li>
    <li class="contact-web">
      <svg class="contact-icon" viewBox="0 0 28 28" aria-hidden="true">
        <polygon points="14,1 26,7.5 26,20.5 14,27 2,20.5 2,7.5" fill="var(--brand-blue)"/>
        <circle cx="14" cy="14" r="4" fill="#fff"/>
      </svg>
      <span class="contact-text">be.profilenet-example.com/in/jorisvandekamp/</span>
    </li>
  </ul>
</section>

</body>
</html>
```